Brindlemoor Client Journey To Success

I need a one-page document that graphically shows the client's journey working with Brindlemoor from initial assessment to completed project. I want the journey to start at the "basecamp logo" and reach 4 summits (little mountain logos...) .

I'd like the imagery to convey the client starting at basecamp, and moving to each summit. Each summit, should list the subtext under each, as listed on the pdf doc i provided.

The description for the basecamp and 4 summits is attached.

I need the brochure to look like the other brochure that you did for me (attached) .

Target Market(s)

Restaurant Owners

Industry/Entity Type

Construction Management

Font styles to use
Sans Serif

Colors
EB3D1F
EC4F4E
F09395
F8D3D4
FCEDEE

Requirements
Must have
• My logo. Title: Client Journey To Success. Subtitle: The 4 Summits

```html
<!DOCTYPE html>
<html lang="en">
<head>
<meta charset="utf-8">
<title>Brindlemoor Client Journey To Success</title>
<link rel="stylesheet" href="https://fonts.googleapis.com/css2?family=Source+Sans+3:wght@400;600;700;800&family=Oswald:wght@500;600&display=swap">
<style>
  :root {
    --page-bg: #e4e4e8;
    --sheet: #ffffff;
    --black: #111111;
    --ink: #2a2a2a;
    --red: #e52421;
    --red-deep: #b8161a;
    --grey-light: #a3a3a3;
    --grey-mid: #6e6e6e;
    --badge-rim: #c9c9c9;
    --text-list: #333333;
  }
  html, body {
    margin: 0;
    width: 1200px;
    height: 1200px;
    overflow: hidden;
    background: var(--page-bg);
  }
  .brochure {
    position: absolute;
    left: 30px;
    top: 160px;
    width: 1140px;
    height: 881px;
    display: block;
    box-shadow: 0 8px 24px rgba(0,0,0,0.18);
  }
  .title { font-family: "Source Sans 3", sans-serif; font-weight: 800; fill: #ffffff; }
  .brand-name { font-family: "Source Sans 3", sans-serif; font-weight: 700; fill: #ffffff; letter-spacing: 0.5px; }
  .arch-label { font-family: "Source Sans 3", sans-serif; font-weight: 800; fill: #ffffff; font-size: 14px; letter-spacing: 0.5px; }
  .flag-number { font-family: "Source Sans 3", sans-serif; font-weight: 800; fill: #ffffff; font-size: 22px; }
  .phase-label { font-family: "Oswald", sans-serif; font-weight: 500; font-size: 14px; }
  .phase-grey { fill: var(--grey-mid); }
  .phase-black { fill: var(--black); }
  .phase-red { fill: var(--red); }
  .step-list { font-family: "Source Sans 3", sans-serif; font-weight: 400; font-size: 9.4px; fill: var(--text-list); }
  .contact { font-family: "Source Sans 3", sans-serif; font-weight: 700; font-size: 12px; fill: #ffffff; }
</style>
</head>
<body>
<svg class="brochure" viewBox="0 0 890 688" xmlns="http://www.w3.org/2000/svg">
  <defs>
    <linearGradient id="headerBand" x1="0" y1="0" x2="0" y2="1">
      <stop offset="0" stop-color="#1c1c1c"/>
      <stop offset="1" stop-color="#050505"/>
    </linearGradient>
    <linearGradient id="subtitleBand" x1="0" y1="0" x2="1" y2="0">
      <stop offset="0" stop-color="#e52421" stop-opacity="0"/>
      <stop offset="0.35" stop-color="#b8161a"/>
      <stop offset="1" stop-color="#e52421"/>
    </linearGradient>
    <linearGradient id="phaseBar" x1="0" y1="0" x2="1" y2="0">
      <stop offset="0" stop-color="#1a1a1a"/>
      <stop offset="0.25" stop-color="#3a1a1a"/>
      <stop offset="0.55" stop-color="#c31b1d"/>
      <stop offset="1" stop-color="#e52421"/>
    </linearGradient>
    <linearGradient id="redArch" x1="0" y1="0" x2="0" y2="1">
      <stop offset="0" stop-color="#d81e20"/>
      <stop offset="1" stop-color="#ef3b35"/>
    </linearGradient>
  </defs>

  <!-- sheet -->
  <rect class="sheet" x="0" y="0" width="890" height="688" fill="var(--sheet)"/>

  <!-- header -->
  <g class="header">
    <rect x="0" y="0" width="890" height="146" fill="url(#headerBand)"/>
    <rect x="0" y="144" width="890" height="7" fill="var(--red)"/>
    <rect x="190" y="72" width="700" height="58" fill="url(#subtitleBand)"/>
    <text class="title" x="523" y="58" font-size="35" text-anchor="middle">CLIENT JOURNEY TO SUCCESS</text>
    <text class="title" x="508" y="116" font-size="37" text-anchor="middle">★ THE 4 SUMMITS ★</text>
    <g class="brand">
      <rect x="67" y="26" width="70" height="70" fill="var(--red)"/>
      <text class="brand-name" x="100" y="128" font-size="10.5" text-anchor="middle">BRINDLEMOOR DEVELOPMENT</text>
    </g>
  </g>

  <!-- arches -->
  <g class="arches" fill="none" stroke-width="26" stroke-linejoin="miter">
    <g class="arch arch-basecamp">
      <path d="M66 508 V435 L148 380 L180 398 V508" stroke="var(--grey-light)"/>
      <text class="arch-label" transform="translate(78 440) rotate(-33)">BASECAMP</text>
    </g>
    <g class="arch arch-summit-1">
      <path d="M214 508 V395 L298 340 L330 358 V508" stroke="var(--grey-mid)"/>
      <text class="arch-label" transform="translate(226 400) rotate(-33)">SUMMIT 1</text>
      <line x1="298" y1="340" x2="298" y2="290" stroke="var(--grey-mid)" stroke-width="1.5"/>
      <path d="M236 280 H298 V308 H236 L246 294 Z" fill="var(--grey-mid)" stroke="none"/>
      <text class="flag-number" x="268" y="303" text-anchor="middle">1</text>
    </g>
    <g class="arch arch-summit-2">
      <path d="M358 508 V360 L441 305 L473 323 V508" stroke="var(--black)"/>
      <text class="arch-label" transform="translate(370 366) rotate(-33)">SUMMIT 2</text>
      <line x1="441" y1="305" x2="441" y2="258" stroke="var(--black)" stroke-width="1.5"/>
      <path d="M383 246 H441 V274 H383 L393 260 Z" fill="var(--black)" stroke="none"/>
      <text class="flag-number" x="413" y="269" text-anchor="middle">2</text>
    </g>
    <g class="arch arch-summit-3">
      <path d="M503 508 V330 L586 275 L618 293 V508" stroke="url(#redArch)"/>
      <text class="arch-label" transform="translate(515 336) rotate(-33)">SUMMIT 3</text>
      <line x1="586" y1="275" x2="586" y2="224" stroke="var(--red)" stroke-width="1.5"/>
      <path d="M528 211 H586 V239 H528 L538 225 Z" fill="var(--red)" stroke="none"/>
      <text class="flag-number" x="558" y="234" text-anchor="middle">3</text>
    </g>
    <g class="arch arch-summit-4">
      <path d="M649 508 V290 L731 235 L763 253 V508" stroke="url(#redArch)"/>
      <text class="arch-label" transform="translate(660 296) rotate(-33)">SUMMIT 4</text>
      <line x1="731" y1="235" x2="731" y2="188" stroke="var(--red-deep)" stroke-width="1.5"/>
      <path d="M671 175 H731 V203 H671 L681 189 Z" fill="var(--red-deep)" stroke="none"/>
      <text class="flag-number" x="702" y="198" text-anchor="middle">4</text>
    </g>
  </g>

  <!-- milestone badges -->
  <g class="badges">
    <g transform="translate(150 470)">
      <polygon points="0,-34 29,-17 29,17 0,34 -29,17 -29,-17" fill="var(--badge-rim)"/>
      <polygon role="img" aria-label="Client assessment icon" points="0,-29 25,-14.5 25,14.5 0,29 -25,14.5 -25,-14.5" fill="#8f8f8f"/>
    </g>
    <g transform="translate(298 430)">
      <polygon points="0,-34 29,-17 29,17 0,34 -29,17 -29,-17" fill="var(--badge-rim)"/>
      <polygon role="img" aria-label="Project plan checklist icon" points="0,-29 25,-14.5 25,14.5 0,29 -25,14.5 -25,-14.5" fill="#5a5a5a"/>
    </g>
    <g transform="translate(441 395)">
      <polygon points="0,-34 29,-17 29,17 0,34 -29,17 -29,-17" fill="var(--badge-rim)"/>
      <polygon role="img" aria-label="Execution gear icon" points="0,-29 25,-14.5 25,14.5 0,29 -25,14.5 -25,-14.5" fill="#2a2a2a"/>
    </g>
    <g transform="translate(586 365)">
      <polygon points="0,-34 29,-17 29,17 0,34 -29,17 -29,-17" fill="var(--badge-rim)"/>
      <polygon role="img" aria-label="Project management icon" points="0,-29 25,-14.5 25,14.5 0,29 -25,14.5 -25,-14.5" fill="var(--red)"/>
    </g>
    <g transform="translate(731 330)">
      <polygon points="0,-34 29,-17 29,17 0,34 -29,17 -29,-17" fill="var(--badge-rim)"/>
      <polygon role="img" aria-label="Mountain summit with flag icon" points="0,-29 25,-14.5 25,14.5 0,29 -25,14.5 -25,-14.5" fill="var(--red-deep)"/>
    </g>
  </g>

  <!-- phase bar -->
  <g class="phase-bar">
    <rect x="0" y="508" width="890" height="57" fill="url(#phaseBar)"/>
    <path d="M203 523 H338 L346 537.5 L338 552 H203 Z" fill="#ffffff"/>
    <path d="M346 523 H473 L481 537.5 L473 552 H346 L354 537.5 Z" fill="#ffffff"/>
    <path d="M481 523 H620 L628 537.5 L620 552 H481 L489 537.5 Z" fill="#ffffff"/>
    <path d="M628 523 H770 L778 537.5 L770 552 H628 L636 537.5 Z" fill="#ffffff"/>
    <text class="phase-label phase-grey" x="270" y="543" text-anchor="middle">PRE-CONSTRUCTION</text>
    <text class="phase-label phase-black" x="413" y="543" text-anchor="middle">EXECUTION</text>
    <text class="phase-label phase-red" x="556" y="543" text-anchor="middle">PROJECT MGMNT</text>
    <text class="phase-label phase-red" x="704" y="543" text-anchor="middle">COMPLETION</text>
    <g class="complete-badge" transform="translate(838 537)">
      <polygon points="0,-38 33,-19 33,19 0,38 -33,19 -33,-19" fill="#9a9a9a"/>
      <polygon points="0,-33 28.5,-16.5 28.5,16.5 0,33 -28.5,16.5 -28.5,-16.5" fill="#2b1414"/>
      <path d="M-14 0 L-4 11 L16 -14" fill="none" stroke="var(--red)" stroke-width="6" stroke-linecap="round" stroke-linejoin="round"/>
    </g>
  </g>

  <!-- step lists -->
  <g class="step-list">
    <text x="48" y="584">
      <tspan x="48">a. Client Assessment</tspan>
      <tspan x="48" dy="12">b. Determine Project</tspan>
      <tspan x="58" dy="12">Goals</tspan>
      <tspan x="48" dy="12">c. Proposal &amp; Fees</tspan>
    </text>
    <text x="201" y="582">
      <tspan x="201">a. Develop Project Plan</tspan>
      <tspan x="201" dy="12">b. Develop Risk Assessment</tspan>
      <tspan x="211" dy="12">&amp; Plan</tspan>
      <tspan x="201" dy="12">c. Devlelop Schedule</tspan>
      <tspan x="201" dy="12">d. Develop Budget</tspan>
      <tspan x="201" dy="12">e. Develop Team</tspan>
      <tspan x="201" dy="12">f. GC, Sub, Consultants Contracts</tspan>
    </text>
    <text x="361" y="582">
      <tspan x="361">a. Acquire Permits</tspan>
      <tspan x="361" dy="12">b. PreConstruction Meeting</tspan>
      <tspan x="361" dy="12">c. Project Start</tspan>
    </text>
    <text x="511" y="582">
      <tspan x="511">a. Shared Consciousness</tspan>
      <tspan x="521" dy="12">Meetings</tspan>
      <tspan x="511" dy="12">b. Pressurized Collaboration</tspan>
      <tspan x="511" dy="12">c. Schedule Management</tspan>
      <tspan x="511" dy="12">d. Run O.O.D.A. Loop</tspan>
    </text>
    <text x="658" y="582">
      <tspan x="658">a. Closeout</tspan>
    </text>
  </g>

  <!-- footer -->
  <g class="footer">
    <rect x="0" y="682" width="890" height="6" fill="var(--red)"/>
    <path d="M498 654 H890 V688 H488 Z" fill="var(--black)"/>
    <path d="M518 654 H690 L680 688 H508 Z" fill="var(--red)"/>
    <path d="M718 654 H890 V688 H708 Z" fill="var(--red)"/>
    <g class="web-icon" fill="none" stroke="#ffffff" stroke-width="1.2">
      <circle cx="508" cy="671" r="5.5"/>
      <line x1="502.5" y1="671" x2="513.5" y2="671"/>
      <ellipse cx="508" cy="671" rx="2.4" ry="5.5"/>
    </g>
    <text class="contact" x="528" y="675">www.brindlemoordev.com</text>
    <rect x="706" y="665.5" width="11" height="11" fill="#ffffff"/>
    <text class="contact" x="740" y="675">@brindlemoordev.com</text>
  </g>
</svg>
</body>
</html>
```